Law firm Seeks Modern and Engaging Site Redesign

Law firm seeks a new web site. Should be modern, but retaining existing logo. Needs to include contact section, professional bio, services offered, and contact information.

The site should be modern, responsive, and able to be SEO optimized.

The finished product should be coded in a Wordpress site, which I will provide. I can work with other platforms, including Wix, but WP is preferred.

Note the current site is https://www.tallowfieldlaw.example/#/home

Target Market(s)

Family Law Practice

Industry/Entity Type

Legal

Coding

Coded - Design and coding required

Number of Pages Required

4 page

Font styles to use
Sans Serif

Requirements
Must have
• Service description
Bio pages for partners
Contact Form
Awards/Publication page

```html
<!DOCTYPE html>
<html lang="en">
<head>
<meta charset="utf-8">
<title>Tallowfield | Marsh — Attorneys at Law</title>
<link rel="stylesheet" href="https://fonts.googleapis.com/css2?family=Lexend:wght@300;400;500&family=Open+Sans:wght@400;600&family=Playfair+Display:wght@700;900&display=swap">
<style>
:root{
  --accent:#4f78e6;
  --brand:#4a5ba3;
  --brand-dark:#3e4d92;
  --navy:#232c55;
  --ink:#2c3550;
  --muted:#6c7080;
  --rule:#e3e5ec;
  --white:#ffffff;
}
*{margin:0;padding:0;box-sizing:border-box}
html,body{width:1200px;height:4099px;overflow:hidden}
body{position:relative;background:var(--white);font-family:"Open Sans",sans-serif;color:var(--ink)}
.abs{position:absolute}
.head{font-family:"Lexend",sans-serif}

/* hero */
.hero{left:0;top:0;width:1200px;height:677px;background:linear-gradient(180deg,#2a3350 0%,#3a4766 45%,#2b3245 100%)}
.photo{background:linear-gradient(180deg,#4a5570,#1f2436)}
.logo{font-family:"Lexend",sans-serif;font-weight:300;font-size:29px;color:var(--white);white-space:nowrap}
.logo-sub{font-family:"Lexend",sans-serif;font-size:11px;color:#c8d0ea}
.nav{left:435px;top:38px;display:flex;gap:22px;font-size:14px;color:var(--white);text-transform:uppercase}
.nav .active{color:#7ea2ff;border-left:2px solid var(--accent);padding-left:10px}
.call-box{left:915px;top:22px;width:208px;height:51px;border:2px solid var(--accent);display:flex;align-items:center;gap:14px;padding-left:16px;color:#9fb6ff;font-family:"Lexend",sans-serif;font-size:16px}
.hero-small{font-family:"Lexend",sans-serif;font-weight:300;color:var(--white);font-size:40px}
.hero-big{font-family:"Playfair Display",serif;font-weight:900;color:var(--white);font-size:84px;line-height:1}
.double{height:6px;border-top:2px solid #e5e8f0;border-bottom:2px solid #e5e8f0}
.btn{background:var(--accent);color:var(--white);font-family:"Lexend",sans-serif;display:flex;align-items:center;justify-content:center;letter-spacing:1px}

/* rated */
.rated-label{left:446px;top:727px;font-size:20px;color:#333}
.badge{left:568px;top:697px;width:185px;height:84px;border:1px solid #ccc;background:#f6f6f6}
.badge span{position:absolute;left:0;bottom:0;width:100%;height:18px;background:#f08a1c}

/* welcome */
.welcome{left:0;top:802px;width:1200px;height:511px;background:var(--brand)}
.frame{left:126px;top:886px;width:294px;height:342px;border:3px solid #6d89e8}
.frame-gap{left:120px;top:1000px;width:310px;height:90px;background:var(--brand)}
.welcome-title{color:var(--white)}
.welcome p{font-size:15px;line-height:27px;color:#eef0fa;width:510px}

/* services */
.section-title{font-family:"Lexend",sans-serif;font-size:42px;color:var(--brand-dark);width:1200px;text-align:center}
.svc-img{width:302px;height:302px}
.svc-head{font-family:"Lexend",sans-serif;font-size:28px;color:var(--brand-dark);border-left:3px solid var(--accent);padding-left:20px;line-height:40px}
.svc-list{list-style:none;font-size:15px;color:#666;line-height:29px}
.learn{font-family:"Lexend",sans-serif;font-size:15px;color:var(--accent)}

/* consult */
.consult{left:0;top:2195px;width:1200px;height:395px;background:linear-gradient(180deg,#3c4a82,#2f3a6a 60%,#3a4777)}
.consult-text{width:1200px;text-align:center;color:var(--white);font-size:28px;line-height:40px}
.consult-text b{color:#6f94ff;font-weight:600}
.call-line{font-family:"Lexend",sans-serif;font-size:43px;color:var(--white);width:1200px;text-align:center}

/* team */
.team-frame{left:87px;top:2500px;width:1024px;height:850px;border:3px solid var(--accent)}
.team-white{left:90px;top:2590px;width:1018px;height:757px;background:var(--white)}
.member-name{font-family:"Lexend",sans-serif;font-size:31px;color:var(--ink)}
.team-list{left:706px;top:2748px;width:340px;list-style:none}
.team-list li{height:68px;display:flex;align-items:center;justify-content:space-between;border-bottom:1px solid var(--rule);font-family:"Lexend",sans-serif;font-size:20px;color:var(--ink)}
.team-list li.current{color:var(--accent)}
.arrow-btn{width:62px;height:62px;background:var(--accent);display:flex;align-items:center;justify-content:center}

/* footer */
.footer{left:0;top:3520px;width:1200px;height:504px;background:linear-gradient(180deg,#2a3463,#1e254a)}
.footer-info{left:110px;width:320px;text-align:center;color:var(--white)}
.field{background:var(--white);font-size:14px;color:#777;padding:16px 18px}
.legal{left:0;top:4048px;width:1200px;text-align:center;font-size:15px;color:var(--brand-dark)}
</style>
</head>
<body>

<!-- hero -->
<div class="abs hero"></div>
<div class="abs photo" style="left:130px;top:165px;width:205px;height:512px;border-radius:90px 90px 0 0" role="img" aria-label="Portrait of a partner in a dark suit and light blue tie"></div>
<div class="abs photo" style="left:880px;top:175px;width:320px;height:502px;border-radius:120px 120px 0 0" role="img" aria-label="Portrait of a partner in a navy suit and striped tie"></div>

<div class="abs logo" style="left:76px;top:20px">Tallowfield | Marsh</div>
<div class="abs logo-sub" style="left:212px;top:58px">Attorneys at Law</div>
<nav class="abs nav">
  <span class="active">Home</span><span>Family Law</span><span>Criminal Law</span><span>About</span><span>Contact</span>
</nav>
<div class="abs call-box">
  <svg width="24" height="24" viewBox="0 0 24 24" fill="none" stroke="#7ea2ff" stroke-width="2"><path d="M5 3h4l2 5-3 2a11 11 0 0 0 6 6l2-3 5 2v4a2 2 0 0 1-2 2A17 17 0 0 1 3 5a2 2 0 0 1 2-2z"/></svg>
  (555) 014 2298
</div>

<div class="abs hero-small" style="left:406px;top:178px">There Is</div>
<div class="abs double" style="left:572px;top:203px;width:218px"></div>
<div class="abs hero-big" style="left:406px;top:238px">No Second</div>
<div class="abs double" style="left:404px;top:350px;width:216px"></div>
<div class="abs hero-small" style="left:641px;top:325px">Place <span style="font-size:18px">In</span></div>
<div class="abs hero-big" style="left:406px;top:395px">Litigation</div>
<div class="abs btn" style="left:423px;top:516px;width:354px;height:62px;font-size:20px">SEE WHAT WE DO</div>

<!-- rated -->
<div class="abs rated-label">Rated By :</div>
<div class="abs badge"><span></span></div>

<!-- welcome -->
<section class="abs welcome"></section>
<div class="abs frame"></div>
<div class="abs frame-gap"></div>
<div class="abs" style="left:120px;top:987px;font-size:14px;color:#fff">Welcome To</div>
<div class="abs head welcome-title" style="left:115px;top:1015px;font-size:40px">Tallowfield | Marsh</div>
<div class="abs head welcome-title" style="left:115px;top:1067px;font-size:26px;letter-spacing:1px">Attorneys At Law</div>
<div class="abs welcome" style="left:563px;top:888px;width:520px;height:auto;background:none">
  <p>The law firm of Tallowfield Marsh, LLC is based in Bergen County, conveniently located in Larkfield, New Jersey in 8 Meridian Plaza. We serve the needs of clients throughout Bergen County, as well as, clients from several other counties, including, but not limited to, Passaic, Morris, Essex and Hudson. Between our partners, we have over 30+ years of experience assisting clients with all of their family law and criminal law needs.</p>
  <p style="margin-top:19px">Often times the areas of family law and criminal law cross paths, which can be both emotionally and financially complex. We understand that our client’s case is unique and pride ourselves on being responsive to all of our clients needs.</p>
</div>

<!-- services -->
<h2 class="abs section-title" style="left:0;top:1380px;font-weight:400">Services We Provide</h2>
<div class="abs svc-img" style="left:274px;top:1473px;background:linear-gradient(135deg,#e9e6df,#c9c3b6)" role="img" aria-label="Young girl resting her head on a table while a parent talks in the background"></div>
<div class="abs svc-img" style="left:626px;top:1473px;background:linear-gradient(135deg,#556070,#3a2a1f)" role="img" aria-label="Hands in handcuffs resting on a wooden table"></div>

<div class="abs svc-head" style="left:272px;top:1810px">Family Law</div>
<ul class="abs svc-list" style="left:298px;top:1871px">
  <li>Divorce</li><li>Child Custody</li><li>Child Support</li><li>Alimony</li><li>Division of Assets and Liabilities</li><li>Pre-nuptial agreements</li><li>High-net worth &amp; complex divorce</li>
</ul>
<div class="abs learn" style="left:295px;top:2092px">Learn More ▸</div>

<div class="abs svc-head" style="left:626px;top:1810px">Criminal Law</div>
<ul class="abs svc-list" style="left:652px;top:1871px">
  <li>Assault</li><li>Domestic Violence</li><li>Drug Crimes</li><li>DWI/DUI</li><li>Sex Crimes</li><li>Theft/Fraud Crimes</li><li>Expungements</li>
</ul>
<div class="abs learn" style="left:647px;top:2092px">Learn More ▸</div>

<!-- consultation -->
<section class="abs consult" role="img" aria-label="Family silhouetted on a beach at dusk, tinted blue"></section>
<div class="abs consult-text" style="left:0;top:2260px">Our legal Team Brings More Than <b>30+ Years</b> of<br>Experience to Assist in all of Your Family Law Needs.</div>
<div class="abs call-line" style="left:0;top:2372px">Call (555) 014-2298</div>
<div class="abs team-frame"></div>
<div class="abs team-white"></div>
<div class="abs btn" style="left:423px;top:2470px;width:354px;height:61px;font-size:20px">SCHEDULE A CONSULTATION</div>

<!-- team -->
<h2 class="abs section-title" style="left:0;top:2655px;font-weight:400">Our Team</h2>
<div class="abs member-name" style="left:170px;top:2783px">Calvin R. Tallowfield</div>
<div class="abs" style="left:173px;top:2830px;font-size:14px;color:#555">Rated By TopCounsel</div>
<p class="abs" style="left:173px;top:2872px;width:400px;font-size:14px;line-height:27px;color:#777">Calvin R. Tallowfield practices in the area of family law, specializing in high conflict matters relating to divorce, custody, equitable distribution, and complex financial issues.</p>
<div class="abs" style="left:173px;top:3010px;width:411px;height:447px;background:linear-gradient(180deg,#d9d3c6,#3a3f52)" role="img" aria-label="Portrait of the partner seated in a leather office chair"></div>
<ul class="abs team-list">
  <li class="current">Calvin R. Tallowfield <span>▸</span></li>
  <li>Jonah P. Marsh <span>▸</span></li>
  <li>Kara D. Whitlow <span>▸</span></li>
  <li>Adriana V. Castellane <span>▸</span></li>
</ul>
<div class="abs arrow-btn" style="left:907px;top:3321px"><svg width="20" height="24" viewBox="0 0 20 24" fill="none" stroke="#fff" stroke-width="2"><path d="M14 2 4 12l10 10"/></svg></div>
<div class="abs arrow-btn" style="left:979px;top:3321px"><svg width="20" height="24" viewBox="0 0 20 24" fill="none" stroke="#fff" stroke-width="2"><path d="m6 2 10 10-10 10"/></svg></div>

<!-- footer -->
<footer class="abs footer" role="img" aria-label="Judge's gavel on a desk, tinted dark blue"></footer>
<div class="abs logo" style="left:110px;top:3620px;width:320px;text-align:center;font-size:31px">Tallowfield | Marsh</div>
<div class="abs logo-sub" style="left:110px;top:3662px;width:320px;text-align:center;color:#fff">Attorneys at Law</div>
<div class="abs head" style="left:110px;top:3700px;width:320px;text-align:center;font-size:36px;color:var(--accent)">(555) 014 2298</div>
<div class="abs footer-info" style="top:3768px;font-size:16px;line-height:25px">Tallowfield &amp; Marsh LLC<br>8 Meridian Plaza Drive Suite 240<br>Larkfield, NJ 07990</div>
<div class="abs footer-info" style="top:3860px;font-size:16px">Fax : (555) 014-2299</div>

<div class="abs field" style="left:545px;top:3615px;width:281px;height:50px">Name *</div>
<div class="abs field" style="left:837px;top:3615px;width:281px;height:50px">Email *</div>
<div class="abs field" style="left:545px;top:3677px;width:281px;height:50px">Phone *</div>
<div class="abs field" style="left:837px;top:3677px;width:281px;height:50px">Practice Area *</div>
<div class="abs field" style="left:545px;top:3739px;width:573px;height:114px">Message *</div>
<div class="abs btn" style="left:545px;top:3869px;width:573px;height:56px;font-size:20px">GET STARTED</div>

<div class="abs legal">©Tallowfield | Marsh -2020 All rights reserved &nbsp;|&nbsp; Sitemap &nbsp;|&nbsp; Legal Disclaimer</div>

</body>
</html>
```